Invitation for Executives

We need an eye-catching design for a direct mail invitation to executives. The invitation will be printed on A3 paper, so the image needs to be very crisp. The invitation details are attached in a word document. Note that the location details etc will be finalised at the end of the contest, so the winner will need to update the final file

Calloway Institute has a special red colour that it uses for all marketing materials - the colour description is Pantone 1807 CMYK C:0 M:91 Y:94 K:30 RGB R:177 G:44 B:27 . Go to the website listed on the invitation details to have a look at the Calloway styles used on the website.
The Calloway logo is CALLOWAY in truesdell font, in the special red colour (or white if that red is the background)

Note - we have decided not to feature the Calloway logo - it will be enough to have the sponsorship byline and link to website, and let the speaker's credentials speak for themselves

Target Market(s)

senior executives (CEO's, CIOs, CFOs ) of major corporates and government agencies. These are busy people, but they are attracted by the idea of networking and mingling with their peers, as well as by the idea of hearing about a world they don't see too often (war zones) Usually they are 50+ years old, and are mostly men (but some women. They usually have pressing problems with the people around them, and want to help develop their teams.

Industry/Entity Type

Marketing

Requirements
Must have
• 1 page only
Nice to have
• something thought provoking or eye catching
Should not have
• any images with references to religion or violence

```html
<!DOCTYPE html>
<html lang="en">
<head>
<meta charset="utf-8">
<title>Conflict Resolution Invitation</title>
<link href="https://fonts.googleapis.com/css2?family=Permanent+Marker&family=Arimo:ital,wght@0,400;0,700;1,400&display=swap" rel="stylesheet">
<style>
  :root {
    --brand-red: #b2140e;
    --ink: #111111;
    --paper: #ffffff;
    --rope-light: #e8d6b4;
    --rope-mid: #c9a878;
    --skin: #e9c2a6;
  }
  html, body { margin: 0; padding: 0; overflow: hidden; background: var(--paper); }
  .invitation {
    position: relative;
    width: 849px;
    height: 1200px;
    overflow: hidden;
    background: var(--paper);
    font-family: "Arimo", Arial, sans-serif;
  }
  .corner-flag { position: absolute; left: 0; top: 0; width: 270px; height: 240px; }
  .sponsor {
    position: absolute; right: 50px; top: 50px;
    text-align: center; color: var(--brand-red); font-size: 18px; line-height: 1.25;
  }
  .sponsor em { font-style: italic; }
  .sponsor a { color: var(--brand-red); font-weight: 700; text-decoration: underline; }
  .tug-photo {
    position: absolute; left: 0; top: 184px; width: 849px; height: 172px;
    background: linear-gradient(90deg, var(--skin) 0%, var(--rope-mid) 18%, var(--rope-light) 50%, var(--rope-mid) 82%, var(--skin) 100%);
    opacity: 0.85;
  }
  .headline {
    position: absolute; left: 0; top: 382px; width: 849px; margin: 0;
    text-align: center; font-family: "Permanent Marker", cursive;
    font-weight: 400; font-size: 47px; line-height: 50px; color: var(--ink);
  }
  .headline .accent { color: var(--brand-red); }
  .details-band {
    position: absolute; left: 0; top: 580px; width: 849px; height: 474px;
    background: var(--brand-red); color: var(--paper);
    box-sizing: border-box; padding: 24px 40px 0;
  }
  .intro { margin: 0; font-size: 23.5px; line-height: 30.5px; text-align: justify; }
  .event {
    margin: 10px 0 0; text-align: center; font-weight: 700;
    font-size: 27.5px; line-height: 35.5px;
  }
  .bio {
    position: absolute; left: 0; top: 1054px; width: 849px; height: 146px;
    box-sizing: border-box; border: 2px solid var(--brand-red); border-top: 0;
    padding: 14px 40px 0; text-align: center;
    font-size: 17.5px; line-height: 20.5px; color: var(--ink);
  }
  .bio p { margin: 0; }
</style>
</head>
<body>
<div class="invitation">

  <svg class="corner-flag" viewBox="0 0 270 240" aria-hidden="true">
    <defs>
      <linearGradient id="curlShade" x1="0" y1="0" x2="1" y2="1">
        <stop offset="0" stop-color="#ffffff"/>
        <stop offset="0.7" stop-color="#eeeeee"/>
        <stop offset="1" stop-color="#b9b9b9"/>
      </linearGradient>
    </defs>
    <polygon points="0,0 262,0 0,226" fill="var(--brand-red)"/>
    <path d="M262,0 C225,70 170,150 40,214 C25,221 10,225 0,226 C60,195 120,190 170,140 C215,95 240,45 262,0 Z" fill="url(#curlShade)"/>
    <g transform="translate(78,96) rotate(-41)" fill="#ffffff" font-family="Arimo, Arial, sans-serif" text-anchor="middle">
      <text x="0" y="0" font-size="27" font-weight="700">Free</text>
      <text x="0" y="28" font-size="20">to Invited Guests</text>
    </g>
  </svg>

  <div class="sponsor">
    Sponsored by <em>Calloway Oceania</em><br>
    <a href="#">www.calloway-institute.example</a>
  </div>

  <div class="tug-photo" role="img" aria-label="Photograph of two pairs of hands pulling on a rope in a tug of war"></div>

  <h1 class="headline">
    <span class="accent">Conflict</span> with the Board<span class="accent">?</span><br>
    <span class="accent">Conflict</span> at Home<span class="accent">?</span><br>
    <span class="accent">Conflict</span> in your Team<span class="accent">?</span>
  </h1>

  <section class="details-band">
    <p class="intro"><strong>Conflict</strong> reduces effectiveness, creates political risk, and can destroy relationships. For inspiration on helping those around you manage conflict, come along to hear <strong>Dr. Reid Hallam</strong>, entrepreneur, academic and <strong>“intercultural peacebuilder”</strong>. Reid has led conflict resolution projects around the world, from boardrooms and government agencies to Middle Eastern and Irish war zones. Join your peers for a fascinating insight into serious conflict and ways to build bridges that endure.</p>
    <p class="event">
      Monday 16th August 2010<br>
      3pm start, 4:30pm networking and nibbles<br>
      The Harbourne Hotel,<br>
      214 Marlow Street<br>
      RSVP 0800 55 21 84
    </p>
  </section>

  <footer class="bio">
    <p><strong>Dr. Hallam</strong> is Assistant Professor at Kalani Pacific University, and was CEO of a successful internet startup sold to <strong>Fieldhouse Media</strong> in 2001. Currently, <strong>Dr. Hallam</strong> is working on a project in the Middle East with the Calloway Institute and CourtBridge International to create sustainable peace among communities in Israel and the West Bank.</p>
  </footer>

</div>
</body>
</html>
```